Where The Cold Rivers Sleep - Movie Poster

I am looking for a poster for my feature film. The movie is a dark thriller called "Where the Cold Rivers Sleep". The movie has not been shot yet and we have not cast the roles so I don't have any images for you to work with. So I am looking for someone to create a poster from scratch, based on the description of the movie. I attached a poster here that is in the ballpark of what I am looking for. The poster for Pale Harbor doesn't show any close up of actors faces but captures the dangerous feeling pf the movie in a way that looks very cool. Looks like a multi million dollar studio film.
Here is a description of my film to give you an idea of what I am looking for: The film is set in a small New England town. The main character (MARK) is a husband whose wife (BRENDA) has created a problem within the family as she has been caught several times stealing from the family's business to support her drug habit. Although she has been trying to get sober, BRENDA is deeply in debt to a ruthless and violent drug dealer. She has even begun prostituting herself as a way of paying back her debt to the drug dealer. MARK's father and brothers have decided to conspire to kill BRENDA for stealing from the business and disgracing the family name. MARK is not willing to get a divorce and is enabling his wife's addiction. In the midst of this conspiracy to kill BERNDA, BRENDA disappears in the woods during a family camping trip with Mark and his brothers. Her body is seen by Mark and his brothers at the bottom of a massive cliff. When they hike to the bottom her body is gone, seemingly devoured by coyotes. The police investigate the crime as if it is a murder and Mark and several of his family members become suspects. It turns out that Brenda faked her own death and was conspiring with one of MARKs brothers (WALLY) to run away together. Wally was taking advantage of BRENDA by paying her for sex and giving her money and drugs. He got her pregnant and convinced her to run away with him. Ultimately BRENDA was unable to leave her husband. MARK forgives Brenda for attempting to run away. He is confronted by the drug dealer. MARK risks his life by attacking the the drug dealer and his thug cronies, killing them all in a shootout, only to find out that his wife is pregnant with his brother's child.
I am looking for someone who can create a HOLLYWOOD looking poster. The poster should communicate an ominous feeling and maybe use some images that you find on your own that capture the essence of the plot.
Thanks!

```html
<!DOCTYPE html>
<html lang="en">
<head>
<meta charset="utf-8">
<title>Where The Cold Rivers Sleep – Poster</title>
<link rel="stylesheet" href="https://fonts.googleapis.com/css2?family=Bebas+Neue&family=Oswald:wght@300&display=swap">
<style>
  :root {
    --page: #ffffff;
    --paper-light: #fbfbfb;
    --paper-shade: #dcdcdc;
    --title-green: #a9d14b;
    --title-pink: #e9268f;
    --title-orange: #f28a35;
    --copy-grey: #5a5a5a;
    --rule-grey: #6f6f6f;
    --rose-light: #f2bfd6;
    --rose-pink: #e58fb6;
    --rose-deep: #c2245c;
    --blood: #a80f34;
    --floor: #f1eff0;
  }
  * { margin: 0; padding: 0; box-sizing: border-box; }
  html, body {
    width: 861px;
    height: 1200px;
    overflow: hidden;
    background: var(--page);
  }
  .poster {
    position: absolute;
    left: 28px;
    top: 30px;
    width: 804px;
    height: 1138px;
    overflow: hidden;
    background: linear-gradient(200deg, var(--paper-light) 0%, #ececec 45%, var(--paper-shade) 62%, var(--floor) 80%, #f6f6f6 100%);
  }
  .title {
    position: absolute;
    left: 46px;
    top: 45px;
    padding: 20px 0;
    font-family: "Bebas Neue", "Oswald", sans-serif;
    font-weight: 400;
    font-size: 164px;
    line-height: 115px;
    letter-spacing: -1px;
    text-transform: uppercase;
    background: linear-gradient(135deg,
      var(--title-green) 0 38%,
      #ffffff 38% 38.6%,
      var(--title-pink) 38.6% 66%,
      #ffffff 66% 66.6%,
      var(--title-orange) 66.6% 100%);
    -webkit-background-clip: text;
    background-clip: text;
    color: transparent;
  }
  .title span { display: block; }
  .synopsis {
    position: absolute;
    left: 56px;
    top: 656px;
    font-family: "Oswald", sans-serif;
    font-weight: 300;
    font-size: 10px;
    line-height: 16px;
    color: var(--copy-grey);
    text-transform: uppercase;
  }
  .accent-rule {
    position: absolute;
    right: 0;
    top: 572px;
    width: 162px;
    height: 1px;
    background: var(--rule-grey);
  }
  .hero-image {
    position: absolute;
    left: 22px;
    top: 668px;
    width: 782px;
    height: 430px;
    background:
      radial-gradient(circle at 78% 30%, var(--blood) 0%, var(--rose-deep) 12%, var(--rose-pink) 28%, var(--rose-light) 42%, rgba(242,191,214,0) 56%),
      radial-gradient(ellipse 30% 16% at 52% 80%, var(--blood) 0%, var(--rose-deep) 40%, rgba(194,36,92,0) 100%),
      radial-gradient(ellipse 26% 12% at 20% 74%, var(--rose-pink) 0%, rgba(229,143,182,0) 100%),
      linear-gradient(180deg, rgba(241,239,240,0) 0%, rgba(242,191,214,0.35) 60%, rgba(241,239,240,0.2) 100%);
  }
</style>
</head>
<body>
  <main class="poster">
    <h1 class="title">
      <span>Where</span>
      <span>The</span>
      <span>Cold</span>
      <span>Rivers</span>
      <span>Sleep</span>
    </h1>
    <p class="synopsis">
      Body copy will be placed here<br>
      The movie is a dark thriller called "Where The Cold Rivers Sleep".<br>
      The movie has not been shot yet and we have not cast the roles so<br>
      I don't have any images for you to work with.
    </p>
    <div class="accent-rule"></div>
    <div class="hero-image" role="img" aria-label="Photograph of a crushed pink rose bleeding dark red liquid, with torn petals and pools of blood on a white surface"></div>
  </main>
</body>
</html>
```